ORB Stationary and Biz cards
Please include the logo I have attached.
Simple
Dorotea Wellmont
dpalvane@qzr.example
www.orbworthkeeping.example
Hello,
I will provide the proper address in a few days. It will take one line for address and one for city and state.
I uploaded the entire file of my logo, not only the AI format. Please let me know if this is a problem. Thank you!
Please let me know if you cannot access the subfiles within this file for your use. Thanks!
Please let me know if you have problems opening the AI file in this attachment. Thank you!
ORB

```html
<!DOCTYPE html>
<html lang="en">
<head>
<meta charset="utf-8">
<title>ORB Business Card</title>
<link href="https://fonts.googleapis.com/css2?family=Source+Sans+3:wght@400;600;700&display=swap" rel="stylesheet">
<style>
  :root {
    --backdrop: #e6e2dc;
    --card-white: #ffffff;
    --frame-blue: #3d93dd;
    --frame-blue-deep: #2f7fc8;
    --brand-blue: #2d7cc4;
    --accent-green: #5aa834;
    --text-grey: #4a4a4a;
    --rule-grey: #b9b9b9;
  }
  * { margin: 0; padding: 0; box-sizing: border-box; }
  html, body {
    width: 1200px; height: 914px; overflow: hidden;
    background: var(--backdrop);
    font-family: "Source Sans 3", "Myriad Pro", Arial, sans-serif;
  }
  .card {
    position: absolute; left: 120px; top: 177px;
    width: 960px; height: 560px;
    background: linear-gradient(135deg, var(--frame-blue), var(--frame-blue-deep));
    padding: 26px;
    box-shadow: 0 4px 14px rgba(0,0,0,0.18);
  }
  .card-face {
    position: relative; width: 100%; height: 100%;
    background: var(--card-white);
  }
  .brand {
    position: absolute; left: 390px; top: 92px;
    display: flex; align-items: center; gap: 14px;
  }
  .brand-dot {
    width: 38px; height: 38px; border-radius: 50%;
    background: var(--accent-green);
  }
  .brand-name {
    font-size: 72px; font-weight: 700; line-height: 1;
    color: var(--brand-blue); letter-spacing: 2px;
  }
  .divider {
    position: absolute; left: 454px; top: 262px;
    width: 1px; height: 146px; background: var(--rule-grey);
  }
  .identity {
    position: absolute; right: calc(100% - 436px); top: 262px;
    text-align: right; color: var(--text-grey);
    font-size: 19px; line-height: 1.4;
  }
  .identity .person-name { color: var(--brand-blue); font-weight: 700; font-size: 21px; }
  .identity .person-role { color: var(--accent-green); font-weight: 600; margin-bottom: 8px; }
  .contacts {
    position: absolute; left: 474px; top: 266px;
    list-style: none; color: var(--text-grey); font-size: 19px;
  }
  .contacts li { display: flex; align-items: center; gap: 10px; height: 34px; }
  .contacts svg { width: 20px; height: 20px; flex: none; }
</style>
</head>
<body>
  <div class="card">
    <div class="card-face">
      <div class="brand">
        <span class="brand-dot"></span>
        <span class="brand-name">ORB</span>
      </div>

      <div class="identity">
        <p class="person-name">Dorotea Wellmont</p>
        <p class="person-role">Owner / C.E.O.</p>
        <p>P.O. Box 4420, Marlow Heights</p>
        <p>VIC 3000</p>
      </div>

      <div class="divider"></div>

      <ul class="contacts">
        <li>
          <svg viewBox="0 0 20 20"><circle cx="10" cy="10" r="10" fill="#2d7cc4"/><path d="M7 5.5l2 2-1 1.3c.6 1.3 1.6 2.3 2.9 2.9l1.3-1 2 2-1.2 1.5c-3.5-.3-7-3.8-7.3-7.3z" fill="#fff"/></svg>
          <span>+00 3 5550 0139</span>
        </li>
        <li>
          <svg viewBox="0 0 20 20"><circle cx="10" cy="10" r="10" fill="#2d7cc4"/><rect x="7" y="4.5" width="6" height="11" rx="1" fill="#fff"/><rect x="8" y="6" width="4" height="6.5" fill="#2d7cc4"/></svg>
          <span>+00 3 5550 0172</span>
        </li>
        <li>
          <svg viewBox="0 0 20 20"><circle cx="10" cy="10" r="10" fill="#2d7cc4"/><rect x="5" y="6.5" width="10" height="7" fill="#fff"/><path d="M5 6.5l5 4 5-4" fill="none" stroke="#2d7cc4" stroke-width="1"/></svg>
          <span>dpalvane@qzr.example</span>
        </li>
        <li>
          <svg viewBox="0 0 20 20"><circle cx="10" cy="10" r="10" fill="#2d7cc4"/><circle cx="10" cy="10" r="5" fill="none" stroke="#fff" stroke-width="1.2"/><path d="M5 10h10M10 5c-2 3-2 7 0 10M10 5c2 3 2 7 0 10" fill="none" stroke="#fff" stroke-width="1"/></svg>
          <span>www.orbworthkeeping.example</span>
        </li>
      </ul>
    </div>
  </div>
</body>
</html>
```